Cool Simple Design for Baby Product

Our company is Lorvanti. We need a package design for our cupboard lock product. We want to appear as caring, warm and close to earth company that aims to improve family life.

Logo is our company logo, colour can be changed if you feel the need for it. Pics 1 and 2 are of the product itself. Pics 3 to 6 are examples of packages and visuals that I do like very much, maybe something along those lines.

Pics 7 and 8 a re just examples of something that I do NOT like. They feel too busy and detailed.

UPDATE: Colourbox1 is the main file that you should work on, colourbox2 is sample of the suppliers default look, so you can see how it looks when it is assembled.

There will be little text, but not much, ALSO there will be text in Germany so please consider this when creating the design. It is not yet finalized what text there will be but something like this:

"Text1: This is English text and there will not be much more than these characters, but also there will be German translation in this same space"

"Text2: Maybe this text too, overall 300 English characters maximum on whole package and that's it"

Industry/Entity Type

Baby

Font styles to use
Decorative
Script

Requirements
Must have
• Simple, soothing, cool, valuable.
Nice to have
• Less is more.
Should not have
• Aggressive with lot of details and too much stuff.

```html
<!DOCTYPE html>
<html lang="en">
<head>
<meta charset="utf-8">
<title>Lorvanti – Magnetic Baby Safety Lock Packaging</title>
<link rel="stylesheet" href="https://fonts.googleapis.com/css2?family=Nunito:ital,wght@0,400;0,600;0,700;0,800;1,800&display=swap">
<style>
  :root {
    --canvas: #ffffff;
    --carton-pink: #fad3e4;
    --carton-fold: #f3b9d2;
    --panel-pink: #f29bc1;
    --frame-pink: #f7c3da;
    --card-white: #ffffff;
    --leaf-green: #6dbd2b;
    --brand-lilac: #c48ac4;
    --brand-circle: #d7c3e6;
    --body-grey: #5b5b5b;
  }
  * { box-sizing: border-box; margin: 0; padding: 0; }
  html, body { width: 846px; height: 1200px; overflow: hidden; background: var(--canvas); }
  body { position: relative; font-family: "Nunito", sans-serif; }

  .brand-header { position: absolute; top: 22px; left: 0; width: 846px; text-align: center; }
  .brand-header__mark { width: 92px; height: 92px; border-radius: 50%; background: var(--brand-circle); margin: 0 auto; }
  .brand-header__name { font-family: "Nunito", sans-serif; font-weight: 600; font-size: 46px; color: var(--brand-lilac); line-height: 1; margin-top: 10px; letter-spacing: 1px; }

  .dieline { position: absolute; left: 0; top: 0; }

  .lid-card { position: absolute; left: 320px; top: 283px; width: 190px; height: 148px; background: var(--frame-pink); padding: 6px; }
  .lid-card__inner { width: 100%; height: 100%; background: var(--card-white); border: 1px solid var(--leaf-green); padding: 5px 6px; position: relative; overflow: hidden; }
  .lid-card h3 { font-size: 5.4px; font-weight: 800; color: var(--leaf-green); line-height: 1.2; margin-top: 3px; }
  .lid-card h3.is-pink { color: #ec7fae; }
  .lid-card h3:first-child { margin-top: 0; font-size: 6px; }
  .lid-card p { font-size: 3.6px; color: var(--body-grey); line-height: 1.35; }
  .lid-card__brand { position: absolute; left: 9px; bottom: 6px; font-size: 6px; font-weight: 600; color: var(--brand-lilac); }

  .side-panel { position: absolute; top: 293px; width: 50px; height: 116px; background: var(--panel-pink); padding: 3px; }
  .side-panel__inner { width: 100%; height: 100%; border: 1px solid #fff; display: flex; align-items: center; justify-content: center; overflow: hidden; }
  .side-panel__text { width: 108px; flex: none; font-size: 5.2px; font-weight: 700; font-style: italic; color: #fff; line-height: 1.3; text-align: center; }
  .side-panel--left { left: 232px; }
  .side-panel--left .side-panel__text { transform: rotate(90deg); }
  .side-panel--right { left: 557px; }
  .side-panel--right .side-panel__text { transform: rotate(-90deg); }

  .front-card { position: absolute; left: 316px; top: 512px; width: 194px; height: 146px; background: var(--frame-pink); padding: 7px; }
  .front-card__inner { width: 100%; height: 100%; background: var(--card-white); border: 1px solid var(--leaf-green); text-align: center; padding-top: 22px; }
  .front-card__brand { font-size: 19px; font-weight: 600; color: var(--brand-lilac); line-height: 1; }
  .front-card__title { margin-top: 16px; font-size: 17px; font-weight: 800; font-style: italic; color: var(--leaf-green); line-height: 1.2; }
</style>
</head>
<body>

<header class="brand-header">
  <div class="brand-header__mark"></div>
  <div class="brand-header__name">lorvanti</div>
</header>

<svg class="dieline" width="846" height="1200" viewBox="0 0 846 1200" role="img" aria-label="Unfolded carton dieline in soft pink with a fine white dot pattern">
  <g fill="var(--carton-pink)">
    <rect x="232" y="205" width="436" height="38" rx="7"/>
    <rect x="150" y="243" width="540" height="193" rx="4"/>
    <rect x="232" y="440" width="436" height="66" rx="6"/>
    <path d="M240 506 H660 V540 H668 V690 Q668 720 640 720 H260 Q232 720 232 690 V540 H240 Z"/>
  </g>
  <g fill="var(--canvas)">
    <rect x="150" y="318" width="10" height="30"/>
    <rect x="680" y="318" width="10" height="30"/>
    <rect x="222" y="322" width="4" height="22" rx="2"/>
    <rect x="614" y="322" width="4" height="22" rx="2"/>
    <rect x="316" y="440" width="4" height="66"/>
    <rect x="512" y="440" width="4" height="66"/>
    <rect x="300" y="690" width="4" height="30"/>
    <rect x="542" y="690" width="4" height="30"/>
  </g>
  <g stroke="var(--carton-fold)" stroke-width="1" fill="none">
    <line x1="232" y1="243" x2="668" y2="243"/>
    <line x1="318" y1="243" x2="318" y2="436"/>
    <line x1="512" y1="243" x2="512" y2="436"/>
    <line x1="230" y1="243" x2="230" y2="436"/>
    <line x1="668" y1="243" x2="668" y2="436"/>
    <line x1="232" y1="438" x2="668" y2="438"/>
    <line x1="232" y1="506" x2="668" y2="506"/>
    <line x1="240" y1="540" x2="660" y2="540"/>
    <line x1="310" y1="506" x2="310" y2="690"/>
    <line x1="518" y1="506" x2="518" y2="690"/>
  </g>
</svg>

<section class="side-panel side-panel--left">
  <div class="side-panel__inner">
    <p class="side-panel__text">This is English text and there will not be much more than these characters, but also there will be German translation in this same space</p>
  </div>
</section>

<section class="lid-card">
  <div class="lid-card__inner">
    <h3>Product Description</h3>
    <p>Every family deserves a calm home where curious little hands stay safe. Our magnetic locks keep cupboards closed without drilling, leaving doors clean and your little one protected every single day.</p>
    <h3 class="is-pink">You can help</h3>
    <p>Help us spread the word by sharing this lock with friends and family who care. Thank you!</p>
    <h3 class="is-pink">Magnetic Baby Safety Lock</h3>
    <p>Strong hidden magnets hold each door shut from the inside. Only the magnetic key opens it, so children cannot reach cleaners, medicine or sharp tools.</p>
    <h3>Installation</h3>
    <p>Clean the surface, peel the adhesive backing and press the lock firmly in place. Wait one day before use so the bond can fully set.</p>
    <h3>100% Money Back Guarantee</h3>
    <p>If you are not fully happy, return it within thirty days for a full refund.</p>
    <h3>#1 in Childproofing Your Home</h3>
    <p>Our locks help parents protect drawers, cabinets and doors all around the home.</p>
    <span class="lid-card__brand">lorvanti</span>
  </div>
</section>

<section class="side-panel side-panel--right">
  <div class="side-panel__inner">
    <p class="side-panel__text">Maybe this text too, overall 300 English characters maximum on whole package and that's it</p>
  </div>
</section>

<section class="front-card">
  <div class="front-card__inner">
    <div class="front-card__brand">lorvanti</div>
    <h1 class="front-card__title">Magnetic Baby<br>safety lock</h1>
  </div>
</section>

</body>
</html>
```